Interior Decorating and Event Styling Business Card Design

We need a business card design for a bespoke interior decorating and event styling business, mostly weddings. We also do custom paint finishes and painted floor finishes. We want something simple, organic and stylish with good colour tones used.

On our card we would like our services listed like so -

Interior Decorating
Wedding and Event Styling
Bespoke furniture paint finishes
Painted floor finishes

Industry/Entity Type

Paint

Contact Information for Business Card

Mara & Wren Design
Rosalind 0438175264
Tessa 0429357718
rosalind.partow@mailbay.com.au
tessaorkin@mwk7.com.au

```html
<!DOCTYPE html>
<html lang="en">
<head>
<meta charset="utf-8">
<title>Mara &amp; Wren Design — Business Card</title>
<link rel="stylesheet" href="https://fonts.googleapis.com/css2?family=Cormorant+Garamond:ital,wght@0,500;0,600;0,700;1,500;1,600&display=swap">
<style>
  :root {
    --page: #ffffff;
    --card-dark: #0a0a0a;
    --card-mid: #2b2b2b;
    --gold: #c9a54a;
    --gold-light: #f1d98a;
    --gold-deep: #8a6a22;
    --text-light: #f2f2f2;
    --text-muted: #9a9a9a;
    --design-grey: #8c8c8c;
  }
  * { box-sizing: border-box; margin: 0; padding: 0; }
  html, body {
    width: 1200px;
    height: 900px;
    overflow: hidden;
    background: var(--page);
  }
  .canvas {
    position: relative;
    width: 1200px;
    height: 900px;
  }
  .card {
    position: absolute;
    top: 271px;
    width: 584px;
    height: 357px;
    background: var(--card-dark);
    overflow: hidden;
    font-family: "Cormorant Garamond", Georgia, serif;
  }
  .card--front { left: 14px; }
  .card--back { left: 604px; }

  .card__pattern {
    position: absolute;
    inset: 0;
    background: radial-gradient(ellipse at 50% 40%, var(--card-mid) 0%, #1a1a1a 45%, var(--card-dark) 100%);
  }
  .card__frame {
    position: absolute;
    inset: 14px;
    border: 5px solid transparent;
    border-image: linear-gradient(90deg, var(--gold-deep), var(--gold-light) 30%, var(--gold) 55%, var(--gold-light) 80%, var(--gold-deep)) 1;
  }

  .brand {
    position: absolute;
    left: 0;
    right: 0;
    text-align: center;
    color: var(--gold);
    font-weight: 600;
    line-height: 1;
  }
  .brand__name { display: block; letter-spacing: 1px; }
  .brand__word { display: block; text-transform: uppercase; }

  .card--front .brand { top: 88px; }
  .card--front .brand__name { font-size: 60px; }
  .card--front .brand__word { font-size: 26px; letter-spacing: 30px; margin-top: 2px; padding-left: 30px; }

  .card--back .brand { top: 36px; }
  .card--back .brand__name { font-size: 32px; }
  .card--back .brand__word { font-size: 14px; letter-spacing: 16px; margin-top: 1px; padding-left: 16px; }

  .flourish {
    position: absolute;
    left: 50%;
    transform: translateX(-50%);
    border-radius: 50%;
    background: radial-gradient(ellipse at center, rgba(241,217,138,0.75) 0%, rgba(201,165,74,0.45) 45%, rgba(201,165,74,0) 75%);
  }
  .card--front .flourish { top: 178px; width: 250px; height: 34px; }
  .card--back .flourish { top: 96px; width: 150px; height: 20px; }

  .contact {
    position: absolute;
    bottom: 44px;
    color: var(--text-light);
    font-size: 19px;
    line-height: 1.35;
    font-weight: 500;
  }
  .contact--left { left: 36px; text-align: left; }
  .contact--right { right: 36px; text-align: right; }
  .contact__name {
    display: block;
    color: var(--gold);
    font-size: 24px;
    font-weight: 700;
    margin-bottom: 4px;
  }
  .contact__phone, .contact__email { display: block; }

  .services {
    position: absolute;
    top: 124px;
    left: 0;
    right: 0;
    list-style: none;
    text-align: center;
    font-style: italic;
    font-weight: 600;
    font-size: 25px;
    line-height: 31px;
    color: var(--text-light);
  }
  .services__item--muted { color: var(--text-muted); }
</style>
</head>
<body>
<main class="canvas">

  <section class="card card--front" aria-label="Business card front">
    <div class="card__pattern" role="img" aria-label="Dark black damask pattern background"></div>
    <div class="card__frame"></div>
    <h1 class="brand">
      <span class="brand__name">Mara &amp; Wren</span>
      <span class="brand__word">Design</span>
    </h1>
    <div class="flourish" role="img" aria-label="Gold scroll ornament"></div>
    <address class="contact contact--left">
      <span class="contact__name">Rosalind</span>
      <span class="contact__phone">0438175264</span>
      <span class="contact__email">rosalind.partow@mailbay.com.au</span>
    </address>
    <address class="contact contact--right">
      <span class="contact__name">Tessa</span>
      <span class="contact__phone">0429357718</span>
      <span class="contact__email">tessaorkin@mwk7.com.au</span>
    </address>
  </section>

  <section class="card card--back" aria-label="Business card back">
    <div class="card__pattern" role="img" aria-label="Dark black damask pattern background"></div>
    <div class="card__frame"></div>
    <h2 class="brand">
      <span class="brand__name">Mara &amp; Wren</span>
      <span class="brand__word">Design</span>
    </h2>
    <div class="flourish" role="img" aria-label="Gold scroll ornament"></div>
    <ul class="services">
      <li class="services__item">Interior Decorating</li>
      <li class="services__item">Wedding and Event Styling</li>
      <li class="services__item services__item--muted">Bespoke furniture paint finishes</li>
      <li class="services__item">Painted floor finishes</li>
    </ul>
  </section>

</main>
</body>
</html>
```